Pflegedienst sucht Flyerdesign
Zielgruppe
Wir sind ein ambulanter Pflegedienst und betreuen ca. 200 Patienten in ländlicher Region. Unsere Zielgruppe sind Pflegebedürftige aus altersbedingten Gründen oder nach Krankenhausaufenthalten. Wir setzen auf Qualität, Zuverlässigkeit, Exklusivität.
Aufgabenstellung
DIN lang Flyer. Wir werben ganz bewußt nicht mit Bildern von Senioren oder alten Menschen, weil das fast alle Pflegedienste tun. Daher setzen wir eher auf Motive aus unserer Urlaubsregion: Strand, Meer...
Unseren Firmen-Vebo hätten wir gern als Fotoausschnitt ohne Hintergund mit dabei.
Und einen Kartenausschnitt mit unserem Einzugsgebiet fänden wir toll. Dies umfasst ca. 15 km um Dünkamp und Holmwik folgende Orte: Stein, Wendtorf, Probsteierhagen, Schönkirchen und Mönkeberg.

```html
<!DOCTYPE html>
<html lang="de">
<head>
<meta charset="utf-8">
<title>Flyer Ambulante Krankenpflege Dünkamp</title>
<link href="https://fonts.googleapis.com/css2?family=Bitter:wght@400;600;700&display=swap" rel="stylesheet">
<style>
:root{
  --magenta:#a8175f;
  --pink:#d67ba7;
  --grey-panel:#ebebeb;
  --ink:#222;
  --white:#fff;
}
*{margin:0;padding:0;box-sizing:border-box}
html,body{width:1200px;height:848px;overflow:hidden;background:var(--white)}
body{font-family:"Bitter",Georgia,serif;color:var(--ink);position:relative}
.panel{position:absolute;top:0;height:848px}
.panel--team{left:0;width:392px;background:var(--grey-panel)}
.panel--contact{left:392px;width:404px;background:var(--white)}
.panel--cover{left:796px;width:404px;background:var(--white)}
.abs{position:absolute}

/* team panel */
.team-title{left:33px;top:34px;font-size:23px;font-weight:700;color:var(--magenta)}
.portrait{width:88px;height:92px;border:3px solid var(--white);background:linear-gradient(160deg,#d9c2b4,#8c7468)}
.person-name{font-size:14px;font-weight:700;color:var(--magenta)}
.person-role{font-size:13.5px;line-height:20px;margin-top:3px}
.quote{left:33px;width:335px;font-size:13.3px;line-height:20px}
.divider{left:33px;width:330px;height:2px;background:var(--magenta)}
.call{left:30px;top:766px;display:flex;align-items:center;gap:12px}
.call-text{font-size:22px;font-weight:700;color:var(--magenta);line-height:29px}

/* contact panel */
.company{left:24px;top:34px;font-size:22px;font-weight:700;color:var(--magenta);line-height:28px}
.address{left:24px;font-size:13.5px;line-height:21.5px}
.address .label{color:var(--magenta)}
.standby{left:24px;top:434px;display:flex;align-items:center;gap:14px}
.standby-text{font-size:21px;font-weight:700;color:var(--magenta);line-height:28px;letter-spacing:.5px}
.car-photo{left:32px;top:532px;width:336px;height:261px;background:linear-gradient(180deg,#9a6e5d 0%,#8b8e90 45%,#7c7a76 100%)}
.car-label{position:absolute;left:0;right:0;bottom:56px;text-align:center;font-size:21px;font-weight:700;color:var(--white)}

/* cover panel */
.cover-photo{left:0;top:0;width:404px;height:534px;background:linear-gradient(180deg,#6f7479 0%,#a49a8e 48%,#3b3631 70%,#6a625a 100%)}
.cover-sub{left:33px;top:52px;font-size:18px;line-height:24px;color:var(--white)}
.cover-head{left:33px;top:104px;font-size:35px;font-weight:700;line-height:37px;color:var(--white)}
.wave{left:0;top:460px}
.badge{left:1014px;top:434px;width:144px;height:144px;border-radius:50%;background:var(--magenta);border:7px solid var(--pink);display:flex;align-items:center;justify-content:center;text-align:center;color:var(--white);font-size:15px;font-weight:700;line-height:20px}
.services{left:24px;top:568px;list-style:none;font-size:15px;line-height:23px}
.services li{padding-left:13px;position:relative}
.services li::before{content:"";position:absolute;left:0;top:9px;width:4px;height:4px;background:var(--magenta);border-radius:50%}
.brand-name{left:24px;top:780px;font-size:20px;line-height:26px;font-weight:700;color:var(--magenta)}
</style>
</head>
<body>

<section class="panel panel--team">
  <h2 class="abs team-title">Ihre Ansprechpartner:</h2>

  <div class="abs portrait" role="img" aria-label="Porträtfoto der Geschäftsleitung" style="left:33px;top:70px"></div>
  <div class="abs" style="left:136px;top:70px">
    <div class="person-name">Moritz Elbe</div>
    <div class="person-role">Geschäftsleitung</div>
  </div>
  <p class="abs quote" style="top:170px">„Einen ambulanten Pflegedienst in Anspruch zu nehmen, bedeutet im ersten Moment, fremden Menschen zu vertrauen.<br>Deswegen möchten wir uns bei einem Erstgespräch vorstellen und uns gegenseitig kennen lernen. Dabei entwickeln wir mit Ihnen, Ihren Angehörigen und unseren Pflegekräften ein auf Sie abgestimmtes individuelles Versorgungskonzept und beraten Sie natürlich gerne auch zur Finanzierung.“</p>
  <div class="abs divider" style="top:357px"></div>

  <div class="abs portrait" role="img" aria-label="Porträtfoto der Pflegedienstleitung" style="left:33px;top:370px"></div>
  <div class="abs" style="left:136px;top:370px">
    <div class="person-name">Anna Brandtke</div>
    <div class="person-role">Pflegedienstleitung Einsatzleitung<br>Holmwik</div>
  </div>
  <p class="abs quote" style="top:468px">„Im Mittelpunkt unserer Bemühungen stehen die Zufriedenheit und die Lebensqualität unserer Patienten. Deswegen begreifen wir unsere Arbeit als einen ständigen Prozess, innerhalb dessen wir die individuelle Situation der Pflegebedürftigen ständig überprüfen, um ihnen die jeweils bestmögliche und auf ihre Bedürfnisse optimal abgestimmte Pflegequalität zukommen lassen zu können.“</p>
  <div class="abs divider" style="top:638px"></div>

  <div class="abs portrait" role="img" aria-label="Porträtfoto der stellvertretenden Pflegedienstleitung" style="left:33px;top:651px"></div>
  <div class="abs" style="left:136px;top:649px">
    <div class="person-name">Svenja Holtkamp</div>
    <div class="person-role">Stellv. Pflegedienstleitung Einsatz-<br>leitung Dünkamp</div>
  </div>

  <div class="abs call">
    <svg width="50" height="50" viewBox="0 0 50 50" aria-hidden="true">
      <circle cx="25" cy="25" r="22" fill="none" stroke="var(--magenta)" stroke-width="5"/>
      <path d="M16 13l6 0 3 7-4 3c2 4 5 7 9 9l3-4 7 3v6c-12 1-25-12-24-24z" fill="var(--magenta)"/>
    </svg>
    <div class="call-text">Rufen Sie uns gerne an:<br>04381 - 4720</div>
  </div>
</section>

<section class="panel panel--contact">
  <h1 class="abs company">Ambulante Krankenpflege<br>Dünkamp GmbH</h1>
  <p class="abs address" style="top:112px"><span class="label">Hauptsitz:</span><br>Lindenweg 7<br>24299 Dünkamp<br>TEL 04381 – 47 20<br>FAX 04381 – 47 29</p>
  <p class="abs address" style="top:240px">info@pflege-duenkamp.de<br>www.pflege-duenkamp.de</p>
  <p class="abs address" style="top:304px"><span class="label">Niederlassung:</span><br>Mühlenstieg 12<br>24288 Holmwik<br>TEL 0437 – 62 14 30 50<br>FAX 0437 – 62 14 30 51</p>
  <div class="abs standby">
    <svg width="50" height="50" viewBox="0 0 50 50" aria-hidden="true">
      <circle cx="25" cy="25" r="22" fill="none" stroke="var(--magenta)" stroke-width="5"/>
      <path d="M16 13l6 0 3 7-4 3c2 4 5 7 9 9l3-4 7 3v6c-12 1-25-12-24-24z" fill="var(--magenta)"/>
    </svg>
    <div class="standby-text">Rufbereitschaft<br>0176 – 93 27 580</div>
  </div>
  <div class="abs car-photo" role="img" aria-label="Foto des beschrifteten Firmenwagens vor einem Backsteinhaus">
    <span class="car-label">freigestellt</span>
  </div>
</section>

<section class="panel panel--cover">
  <div class="abs cover-photo" role="img" aria-label="Abendstimmung am Strand mit Turm und Spiegelung im Wasser"></div>
  <p class="abs cover-sub">Ambulante Krankenpflege<br>Dünkamp &amp; Holmwik</p>
  <h2 class="abs cover-head">Ihr Premiumdienst<br>in der Region</h2>
  <svg class="abs wave" width="404" height="74" viewBox="0 0 404 74" aria-hidden="true">
    <path d="M0 40 C120 36 260 24 404 0 L404 16 C260 38 120 48 0 50Z" fill="#fff"/>
    <path d="M0 50 C120 48 260 38 404 16 L404 74 L0 74Z" fill="var(--magenta)"/>
  </svg>
  <ul class="abs services">
    <li>Häusliche Pflege</li>
    <li>Pflegeberatung</li>
    <li>Demenzbetreuung</li>
    <li>Aktivierende Beschäftigung</li>
    <li>Entlastung im Haushalt</li>
    <li style="margin-top:3px">Palliativpflege Sterbebegleitung<br>24 h Rufbereitschaft</li>
  </ul>
  <p class="abs brand-name">Pflegedienst Dünkamp</p>
</section>

<div class="abs badge">Von<br>Mensch zu<br>Mensch seit<br>über 20<br>Jahren</div>

</body>
</html>
```